Tri fold brochure + business cards

I would like a tri fold brochure made and dual sided business cards. It will need to include text, graphics and screenshots from our company app. On the brochure I would like an image of a map with a pin dropped in the center of a mapped circular radius that pin should say "Your Store" and within the radius pins with random person "customer" faces. I have text I would like to add on the brochure which will be provided. I would also like an image with a process map showing how order process Customer submits order, seller accepts request, order details sent to tavrenko, tavrenko organizes delivery driver, delivery driver arrives to seller to collect item and displays order number, delivery driver delivers order to buyer. I would like this process shown graphically and a timeline shown about this process of 1 hour. I have other screenshots I would like to use to show a how to use section for different functions of the app. I'm open to your interpretation for business cards but they should include tavrenko icon.

```html
<!DOCTYPE html>
<html lang="en">
<head>
<meta charset="utf-8">
<title>Tavrenko business cards</title>
<link rel="stylesheet" href="https://fonts.googleapis.com/css2?family=Open+Sans:wght@400;600;700&display=swap">
<style>
  :root {
    --page-bg: #e6e8e6;
    --card-white: #ffffff;
    --lime: #cfe22a;
    --leaf: #4cb62e;
    --ink-green: #1e5a1e;
    --bright-green: #5cc234;
    --logo-dark: #221f20;
    --logo-dark-2: #3a3637;
    --rule-dark: #1b1b1b;
    --text-dark: #1d2a12;
  }
  * { box-sizing: border-box; margin: 0; padding: 0; }
  html, body { width: 1200px; height: 900px; overflow: hidden; }
  body {
    background: var(--page-bg);
    font-family: "Open Sans", Arial, sans-serif;
    position: relative;
  }
  .card {
    position: absolute;
    top: 301px;
    width: 520px;
    height: 297px;
    border-radius: 4px;
    box-shadow: 0 8px 22px rgba(0,0,0,0.18);
    overflow: hidden;
  }
  .brand-square {
    position: absolute;
    background: radial-gradient(circle at 50% 40%, var(--logo-dark-2), var(--logo-dark) 70%);
    display: flex; align-items: center; justify-content: center;
  }
  .brand-name {
    color: var(--bright-green);
    font-weight: 700;
    font-size: 24px;
    letter-spacing: 0.5px;
  }

  /* contact side */
  .card-back { left: 53px; background: var(--card-white); }
  .card-back .brand-square { left: 30px; top: 58px; width: 166px; height: 166px; }
  .card-back .divider {
    position: absolute; left: 214px; top: 30px;
    width: 4px; height: 236px;
    background: var(--rule-dark);
  }
  .card-back .divider-accent {
    position: absolute; left: 214px; top: 108px;
    width: 4px; height: 64px;
    background: var(--bright-green);
  }
  .contact-list { position: absolute; left: 232px; top: 28px; right: 14px; }
  .contact-row { display: flex; align-items: flex-start; margin-bottom: 11px; }
  .pill {
    flex: none;
    width: 46px; height: 22px; border-radius: 11px;
    background: var(--bright-green);
    display: flex; align-items: center; padding-left: 3px;
    margin-right: 12px; margin-top: 3px;
  }
  .pill .dot {
    width: 16px; height: 16px; border-radius: 50%;
    background: var(--card-white);
    display: flex; align-items: center; justify-content: center;
  }
  .pill svg { width: 10px; height: 10px; }
  .contact-text { color: var(--ink-green); font-size: 12px; line-height: 1.4; }
  .person-name { font-size: 17px; font-weight: 700; letter-spacing: 0.5px; line-height: 1.2; }
  .person-role { font-size: 11.5px; }

  /* logo side */
  .card-front {
    left: 627px;
    background: linear-gradient(215deg, var(--leaf) 0%, #8fcf2a 50%, var(--lime) 100%);
  }
  .card-front .brand-square { left: 186px; top: 38px; width: 148px; height: 148px; }
  .card-front .site-url {
    position: absolute; left: 0; right: 0; top: 204px;
    text-align: center; color: var(--text-dark); font-size: 14px; font-weight: 600;
  }
</style>
</head>
<body>
  <section class="card card-back" aria-label="Business card contact side">
    <div class="brand-square"><span class="brand-name">tavrenko</span></div>
    <div class="divider"></div>
    <div class="divider-accent"></div>
    <div class="contact-list">
      <div class="contact-row">
        <span class="pill"><span class="dot"><svg viewBox="0 0 10 10"><circle cx="5" cy="3.2" r="2.2" fill="#1e5a1e"/><path d="M1 10c0-3 2-4.3 4-4.3S9 7 9 10z" fill="#1e5a1e"/></svg></span></span>
        <div class="contact-text"><div class="person-name">MILIYOO TAVRENKO</div><div class="person-role">CO-Founder</div></div>
      </div>
      <div class="contact-row">
        <span class="pill"><span class="dot"><svg viewBox="0 0 10 10"><path d="M2.2 1l1.6 2-1 1c.6 1.3 1.3 2 2.6 2.6l1-1 2 1.6-1 1.6C4.6 8.6 1.4 5.4 1 2z" fill="#1e5a1e"/></svg></span></span>
        <div class="contact-text">+44-0200-114-820<br>+44-0200-557-193</div>
      </div>
      <div class="contact-row">
        <span class="pill"><span class="dot"><svg viewBox="0 0 10 10"><rect x="1" y="2.2" width="8" height="5.6" fill="none" stroke="#1e5a1e" stroke-width="1"/><path d="M1 2.4l4 3 4-3" fill="none" stroke="#1e5a1e" stroke-width="1"/></svg></span></span>
        <div class="contact-text">hello@tavrenko.app<br>office@tavrenko.app</div>
      </div>
      <div class="contact-row">
        <span class="pill"><span class="dot"><svg viewBox="0 0 10 10"><circle cx="5" cy="5" r="4" fill="none" stroke="#1e5a1e" stroke-width="1"/><ellipse cx="5" cy="5" rx="1.8" ry="4" fill="none" stroke="#1e5a1e" stroke-width="0.8"/><path d="M1 5h8" stroke="#1e5a1e" stroke-width="0.8"/></svg></span></span>
        <div class="contact-text">www.tavrenko.app<br>www.tavrenkodelivery.com</div>
      </div>
      <div class="contact-row">
        <span class="pill"><span class="dot"><svg viewBox="0 0 10 10"><path d="M5 9.5S1.8 6 1.8 3.8a3.2 3.2 0 016.4 0C8.2 6 5 9.5 5 9.5z" fill="#1e5a1e"/><circle cx="5" cy="3.8" r="1.1" fill="#fff"/></svg></span></span>
        <div class="contact-text">Unit 12, Harbor Lane<br>Leeds, United Kingdom</div>
      </div>
    </div>
  </section>

  <section class="card card-front" aria-label="Business card logo side">
    <div class="brand-square"><span class="brand-name">tavrenko</span></div>
    <p class="site-url">www.tavrenko.app</p>
  </section>
</body>
</html>
```